SkyvornQ Business Cards and Stationary Design

Need a design for our business cards and stationary. I want to carry on the theme of the logo. I want the business cards to have a design on the back. I would like the business cards and the stationary to carry the same theme, design scheme, and branding

Target Market(s)

Airlines and Maintenance Facilities

Industry/Entity Type

Aviation

Contact Information for Business Card

Address: 4827 Tallowmere Lane, Marlow Bay, Coraston, 34951

Font styles to use
Serif
Sans Serif

Colors

Designer to choose colors to be used in the design.

```html
<!DOCTYPE html>
<html lang="en">
<head>
<meta charset="utf-8">
<title>SkyvornQ Business Card</title>
<link href="https://fonts.googleapis.com/css2?family=Work+Sans:wght@400;700&display=swap" rel="stylesheet">
<style>
  :root {
    --backdrop: #262626;
    --card-white: #ffffff;
    --brand-navy: #14284f;
    --brand-blue: #27a2dc;
    --ink: #3a3a3a;
    --divider: #5ab2e0;
  }
  * { margin: 0; padding: 0; box-sizing: border-box; }
  html, body { width: 1200px; height: 800px; overflow: hidden; }
  body {
    background: var(--backdrop);
    font-family: "Work Sans", sans-serif;
    position: relative;
  }
  .card {
    position: absolute;
    left: 347px;
    width: 499px;
    height: 284px;
  }
  .card-front { top: 110px; background: var(--card-white); }
  .card-back { top: 417px; background: var(--brand-blue); }

  .front-brand {
    position: absolute;
    left: 23px; top: 76px;
    width: 240px;
    text-align: center;
  }
  .brand-dot {
    display: block;
    margin: 0 auto 6px;
    width: 64px; height: 64px;
    border-radius: 50%;
    border: 6px solid var(--brand-navy);
  }
  .brand-name {
    font-weight: 700;
    font-size: 28px;
    line-height: 1;
    letter-spacing: 4px;
    color: var(--brand-navy);
  }
  .front-divider {
    position: absolute;
    left: 272px; top: 72px;
    width: 1px; height: 112px;
    background: var(--divider);
  }
  .contact {
    position: absolute;
    left: 300px; top: 70px;
  }
  .contact-name {
    font-size: 19px;
    font-weight: 400;
    letter-spacing: 0.6px;
    color: var(--brand-blue);
    line-height: 1.1;
  }
  .contact-title {
    font-size: 11px;
    letter-spacing: 0.6px;
    color: var(--ink);
    margin-top: 2px;
  }
  .contact-list { list-style: none; margin-top: 20px; }
  .contact-list li {
    display: flex; align-items: center;
    font-size: 11.5px;
    letter-spacing: 0.4px;
    color: var(--ink);
    height: 15px;
  }
  .contact-list svg { width: 8px; height: 8px; margin-right: 8px; flex: none; }
  .address {
    position: absolute;
    left: 0; right: 0; top: 242px;
    text-align: center;
    font-size: 11.5px;
    letter-spacing: 0.4px;
    color: var(--ink);
  }

  .back-brand {
    position: absolute;
    left: 0; right: 0; top: 53px;
    text-align: center;
  }
  .back-brand .brand-dot {
    width: 96px; height: 96px;
    border: 6px solid var(--card-white);
    margin-bottom: 12px;
  }
  .back-brand .brand-name {
    font-size: 40px;
    letter-spacing: 8px;
    color: var(--card-white);
  }
  .back-url {
    position: absolute;
    left: 0; right: 0; top: 241px;
    text-align: center;
    font-size: 13px;
    font-weight: 700;
    color: var(--card-white);
  }
</style>
</head>
<body>
  <section class="card card-front">
    <div class="front-brand">
      <span class="brand-dot"></span>
      <div class="brand-name">SKYVORNQ</div>
    </div>
    <div class="front-divider"></div>
    <div class="contact">
      <div class="contact-name">DALEN MARSH</div>
      <div class="contact-title">CEO/Founder</div>
      <ul class="contact-list">
        <li><svg viewBox="0 0 8 8"><rect x="1.5" y="0.5" width="5" height="7" rx="1" fill="none" stroke="#27a2dc"/></svg>555-214-0976</li>
        <li><svg viewBox="0 0 8 8"><path d="M1 1 L3 1 L3.5 3 L2.5 3.7 Q3.5 5.5 5 6 L5.6 5 L7.5 5.5 L7.5 7.3 Q2 7.5 1 1Z" fill="#27a2dc"/></svg>555-214-0976</li>
        <li><svg viewBox="0 0 8 8"><rect x="0.5" y="1.5" width="7" height="5" fill="none" stroke="#27a2dc"/><path d="M0.5 1.5 L4 4.5 L7.5 1.5" fill="none" stroke="#27a2dc"/></svg>www.mailsample.com</li>
        <li><svg viewBox="0 0 8 8"><circle cx="4" cy="4" r="3.5" fill="none" stroke="#27a2dc"/><path d="M0.5 4 H7.5 M4 0.5 V7.5" stroke="#27a2dc"/></svg>www.skyvornq.com</li>
      </ul>
    </div>
    <p class="address">4827 Tallowmere Lane, Marlow Bay, Coraston, 34951</p>
  </section>

  <section class="card card-back">
    <div class="back-brand">
      <span class="brand-dot"></span>
      <div class="brand-name">SKYVORNQ</div>
    </div>
    <p class="back-url">www.skyvornq.com</p>
  </section>
</body>
</html>
```